Brindle Children's Center - Child Care brochure

I just bought a new child care and completely renovated the space. We are also designing a new website, so I need the brochure to match that with updated info. www.brindlechildrenscenter.com - Information on there is current. We expect to have the new one up and running in the next few days. We have new photo's that I'd like to be added to the flyer too. ps. the boys in the pictures are mine, so i would appreciate one of them being added :). support@pixelhavenweb.com has details on the website (dev.brindlechildrenscenter.com). The child care program is only open during the ski season - i.e. a resort facility catering to high end clients.
I'm attaching the the website information, the flyer I created, logo files and pictures.

dev.brindlechildrenscenter.com Added Sunday, September 24, 2017

Target Market(s)

Parents of young children

Font styles to use
Other font styles liked:
• "Things we said" & "Calibri Light"

Colors
cfeae6
fef1ee

Requirements
Must have
• Pictures of children. sleek design - winter, mountain theme. Check with website designer on new website.
Nice to have
• prices included
Should not have
• Kid like artwork

```html
<!DOCTYPE html>
<html lang="en">
<head>
<meta charset="utf-8">
<title>Brindle Children's Center – Brochure</title>
<link href="https://fonts.googleapis.com/css2?family=Caveat:wght@500;700&family=Lato:wght@300;400;700&display=swap" rel="stylesheet">
<style>
:root{
  --teal:#7cc4bd;
  --teal-dark:#4fa59d;
  --mint:#cfeae6;
  --blush:#fef1ee;
  --ink:#5b6468;
  --paper:#ffffff;
  --photo-warm:#c9a58a;
  --photo-cool:#a9bfc6;
}
*{box-sizing:border-box;margin:0;padding:0}
html,body{width:829px;height:1200px;overflow:hidden;background:#fff}
body{position:relative;font-family:'Lato',sans-serif;color:var(--ink);font-weight:300}
.spread{position:absolute;left:14px;width:801px;display:flex;background:var(--paper);box-shadow:0 1px 4px rgba(0,0,0,.18)}
.spread.outside{top:32px;height:520px}
.spread.inside{top:592px;height:572px}
.panel{position:relative;width:267px;height:100%;overflow:hidden;padding:14px 16px}
.panel+.panel{border-left:1px solid #eef2f2}
.photo{position:absolute;display:block}
.warm{background:linear-gradient(135deg,#d9bda6,#b98f73 60%,#8f6d58)}
.cool{background:linear-gradient(135deg,#dfe8ea,#a9bfc6 60%,#7f969e)}
.snow{background:linear-gradient(180deg,#b7c9d6,#e8eef2 55%,#9c8b7a)}
h2,h3{font-family:'Caveat',cursive;color:var(--teal-dark);font-weight:700}
h2{font-size:27px;line-height:1}
h3{font-size:19px;margin:8px 0 2px}
p,li{font-size:7.4px;line-height:1.45}
ul{list-style:none}
.price{display:flex;justify-content:space-between;font-size:7.6px;line-height:1.6}
.price b{font-weight:700;color:var(--teal-dark)}
.teal-band{position:absolute;left:0;right:0;background:var(--mint)}
.brand{display:flex;align-items:center;gap:6px;font-family:'Caveat',cursive;font-weight:700;color:var(--teal-dark)}
.brand .dot{width:14px;height:14px;border-radius:50%;background:var(--teal)}
.web{font-size:8px;color:var(--teal-dark);font-weight:700}
</style>
</head>
<body>

<!-- OUTSIDE SPREAD -->
<section class="spread outside">
  <div class="panel pricing">
    <h2>Pricing</h2>
    <ul style="margin-top:6px">
      <li class="price"><span>Full Day</span><b>$145</b></li>
      <li>8:30am – 4:30pm, lunch and snacks included</li>
      <li class="price" style="margin-top:6px"><span>Half Day</span><b>$95</b></li>
      <li>8:30am – 12:30pm or 12:30pm – 4:30pm</li>
      <li class="price" style="margin-top:6px"><span>5-Day Package</span><b>$650</b></li>
      <li>Five full days to use any time during the season. Packages must be booked in advance and are non-refundable.</li>
    </ul>
    <p style="margin-top:8px">A 20% deposit holds your child's spot. Cancellations made at least 48 hours before the booked date receive a full credit toward a future visit this season.</p>
    <ul style="margin-top:8px">
      <li class="price"><span>Ages 2–3 Full Day</span><b>$155</b></li>
      <li class="price"><span>Ages 3–5 Full Day</span><b>$145</b></li>
      <li class="price"><span>Ages 5–8 Full Day</span><b>$135</b></li>
      <li class="price"><span>Sibling Discount</span><b>10%</b></li>
      <li class="price"><span>Late Pickup / 15 min</span><b>$15</b></li>
    </ul>
    <div class="photo warm" role="img" aria-label="Photo of children playing at a table" style="left:0;bottom:0;width:267px;height:148px"></div>
  </div>

  <div class="panel contact">
    <div class="photo snow" role="img" aria-label="Photo of the snowy mountain chalet building" style="left:0;top:0;width:267px;height:118px"></div>
    <div class="brand" style="position:absolute;top:128px;left:0;right:0;justify-content:center;font-size:16px"><span class="dot"></span>Brindle</div>
    <div style="position:absolute;top:158px;left:18px;right:18px;text-align:center">
      <h3>Questions? Contact</h3>
      <p>Our friendly staff is happy to help you plan your family's stay. Call or email us any time during the ski season and we will reply within one business day with availability and details.</p>
      <p style="margin-top:6px">We look forward to welcoming your little ones to the mountain this winter.</p>
    </div>
    <div class="photo cool" role="img" aria-label="Photo of a child with a teacher" style="left:18px;top:268px;width:231px;height:96px"></div>
    <div class="teal-band" style="bottom:0;height:140px;background:var(--teal);color:#fff;text-align:center;padding:18px 16px">
      <h3 style="color:#fff;margin:0 0 6px">Contact Us</h3>
      <p>124 Powder Ridge Lane, Suite 2<br>Summit Village, CO 80435</p>
      <p style="margin-top:4px">(970) 555-0148</p>
      <p style="margin-top:4px">hello@brindlechildrenscenter.com</p>
      <p class="web" style="color:#fff;margin-top:8px">www.brindlechildrenscenter.com</p>
    </div>
  </div>

  <div class="panel cover" style="padding:0">
    <svg width="267" height="120" style="position:absolute;top:0;left:0" aria-hidden="true">
      <path d="M0 0H267V80Q133 130 0 80Z" fill="var(--mint)"/>
    </svg>
    <div class="brand" style="position:absolute;top:30px;left:0;right:0;justify-content:center;font-size:20px"><span class="dot"></span>Brindle</div>
    <div class="photo warm" role="img" aria-label="Portrait photo of a smiling young boy" style="left:0;top:110px;width:267px;height:300px"></div>
    <div class="photo cool" role="img" aria-label="Photo of a child in winter clothing" style="left:18px;top:352px;width:90px;height:90px;border-radius:50%;border:4px solid #fff"></div>
    <div style="position:absolute;left:0;right:0;bottom:30px;text-align:center">
      <h2 style="font-size:24px;color:var(--ink)">Brindle Children's Center</h2>
    </div>
  </div>
</section>

<!-- INSIDE SPREAD -->
<section class="spread inside">
  <div class="panel">
    <div class="teal-band" style="top:0;height:22px"></div>
    <h2 style="margin-top:14px">Brindle Children's Center</h2>
    <p style="margin-top:6px">Our mission is to ensure that all children in our care are safe, happy and engaged while their parents enjoy the mountain.</p>
    <p style="margin-top:6px">Nestled at the base of the slopes, our fully renovated center offers bright classrooms, cozy nap rooms and a secure outdoor play area. Our experienced teachers plan each day around play, discovery and rest, so every child leaves with new friends and stories to share.</p>
    <h3>Our Mission</h3>
    <p>We provide a warm, caring home away from home for visiting families. We nurture curiosity, kindness and confidence through hands-on learning, creative play and plenty of fresh mountain air.</p>
    <h3>Our Values</h3>
    <p>Safety comes first in everything we do. Our staff are certified in first aid and CPR, and we keep small group sizes so each child gets the attention they deserve. We value respect, patience, open communication with parents and a calm, joyful environment.</p>
    <div class="photo warm" role="img" aria-label="Photo of children painting together" style="left:0;bottom:0;width:267px;height:140px"></div>
  </div>

  <div class="panel">
    <div class="photo cool" role="img" aria-label="Photo of a teacher reading to children" style="left:0;top:0;width:267px;height:150px"></div>
    <div style="position:absolute;top:162px;left:16px;right:16px">
      <p>In the Brindle Children's Center, our staff take pride in creating a nurturing and creative environment where your child can play, learn and grow. Each morning begins with a welcome circle, songs and a story before we head into themed activity stations.</p>
      <p style="margin-top:6px">Our rooms are filled with books, blocks, art supplies and sensory tables. We offer healthy snacks and a warm lunch, and every child enjoys quiet time in a soft, restful space.</p>
      <p style="margin-top:6px">Parents receive a short daily note describing meals, naps and favorite moments, so you always know how your little one spent the day.</p>
    </div>
    <div class="photo warm" role="img" aria-label="Photo of toddlers playing with toys" style="left:0;bottom:0;width:267px;height:180px"></div>
  </div>

  <div class="panel">
    <p>We would love to hear from you before your visit. Reserve early to secure a place during the busiest holiday weeks.</p>
    <h3>Activities</h3>
    <p>Each day includes music and movement, arts and crafts, building challenges, pretend play and snow exploration when the weather allows. Children are grouped by age so every activity matches their stage of development.</p>
    <h3>Philosophy</h3>
    <p>We believe children learn best through play. Our teachers follow each child's interests, encourage independence and celebrate small victories. We create a calm, predictable routine so children feel secure in a new place.</p>
    <p style="margin-top:6px">The Brindle Children's Center is open only during the ski season, welcoming families from around the world.</p>
    <p class="web" style="margin-top:8px">www.brindlechildrenscenter.com</p>
    <div class="photo cool" role="img" aria-label="Photo of a child playing with blocks" style="left:0;bottom:0;width:267px;height:190px"></div>
  </div>
</section>

</body>
</html>
```